Infographic representing workforce

Hello - I would like an infographic created to insert into a document to represent the composition of our workforce.
I've attached one very casual idea below but do NOT like the pink! Would prefer something a little more professional / modern.
Here is the information:
TOTAL EMPLOYEES
25
DIVERSITY
White: 60%
Asian: 24%
Hispanic: 8%
Middle-Eastern: 8%
AGE
25 - 44: 32%
45 - 64: 56%
65+: 12%
GENDER
Female: 60%
Male: 40%
EXECUTIVE OFFICERS
2of 3 are women
BOARD COMPOSITION
50% women (3 directors)
One woman from an unrepresented community

```html
<!DOCTYPE html>
<html lang="en">
<head>
<meta charset="utf-8">
<title>Our Workforce</title>
<link href="https://fonts.googleapis.com/css2?family=Montserrat:wght@400;500;600;700&family=Nunito:wght@800;900&display=swap" rel="stylesheet">
<style>
  :root {
    --navy: #1557a6;
    --blue: #0a79bf;
    --sky: #7badd9;
    --mist: #cfe0f2;
    --band: #c5dbef;
    --accent: #e3202a;
    --ink: #1c1c1c;
    --grey: #8a8a8a;
    --panel-end: #e6eff9;
    --rule: #bfc9d4;
  }
  * { margin: 0; padding: 0; box-sizing: border-box; }
  html, body { width: 1200px; height: 997px; overflow: hidden; background: #ffffff; }
  body { font-family: "Montserrat", sans-serif; color: var(--ink); }

  .stage {
    position: absolute; left: 0; top: 7px;
    width: 1500px; height: 1227px;
    transform: scale(0.8); transform-origin: 0 0;
    background: #ffffff;
  }
  .diversity-panel {
    position: absolute; left: 0; top: 0; width: 990px; height: 1227px;
    background: linear-gradient(180deg, #ffffff 40%, var(--panel-end) 100%);
  }
  .graphics { position: absolute; left: 0; top: 0; width: 1500px; height: 1227px; }

  .t { position: absolute; white-space: nowrap; line-height: 1; }
  .c { transform: translate(-50%, -50%); text-align: center; }
  .l { transform: translateY(-50%); }

  .title-our { left: 129px; top: 248px; font-size: 50px; font-weight: 500; color: var(--grey); letter-spacing: 1px; }
  .title-main { left: 116px; top: 304px; font-size: 95px; font-weight: 600; color: var(--navy); letter-spacing: 1px; }

  .team-art { position: absolute; left: 302px; top: 35px; width: 435px; height: 257px;
    background: linear-gradient(180deg, #dbe8f5 0%, #b9d0e8 100%); border-radius: 10px; }
  .avatar { position: absolute; width: 142px; height: 142px; border-radius: 50%; transform: translate(-50%, -50%); }
  .avatar.me { left: 177px; top: 487px; background: linear-gradient(180deg, #9cc1e4 0%, var(--sky) 100%); }
  .avatar.hi { left: 795px; top: 495px; background: linear-gradient(180deg, #e0ebf7 0%, var(--mist) 100%); }
  .avatar.as { left: 159px; top: 993px; background: linear-gradient(180deg, #2f92d0 0%, var(--blue) 100%); }
  .avatar.wh { left: 825px; top: 1002px; background: linear-gradient(180deg, #2f6fba 0%, var(--navy) 100%); }

  .pct-big { font-family: "Nunito", sans-serif; font-weight: 900; font-size: 46px; color: var(--sky); }
  .group-label { font-size: 22px; font-weight: 500; }

  .total-label { left: 517px; top: 723px; font-family: "Nunito", sans-serif; font-weight: 900; font-size: 33px; line-height: 36px; color: var(--navy); }
  .total-value { left: 517px; top: 812px; font-family: "Nunito", sans-serif; font-weight: 900; font-size: 128px; color: var(--sky); }
  .diversity-label { left: 512px; top: 1055px; font-size: 21px; font-weight: 500; background: #f1f6fc; padding: 2px 6px; }

  .section-title { font-family: "Nunito", sans-serif; font-weight: 900; font-size: 26px; color: var(--ink); letter-spacing: 0.3px; }
  .axis { font-size: 15px; font-weight: 500; text-align: right; }
  .bar-val { font-family: "Nunito", sans-serif; font-weight: 900; font-size: 21px; color: #ffffff; }
  .bar-cat { font-size: 18px; font-weight: 500; }

  .gender-pct { font-size: 42px; font-weight: 500; }
  .gender-pct small { font-size: 24px; }
  .gender-pct.male { left: 1112px; top: 587px; color: var(--navy); }
  .gender-pct.female { left: 1365px; top: 587px; color: var(--blue); }
  .gender-tag { font-size: 15px; font-weight: 500; }

  .note { font-size: 21px; font-weight: 500; line-height: 26px; white-space: nowrap; }
  .ring-value { left: 1119px; top: 1033px; font-size: 40px; font-weight: 500; color: var(--sky); }
  .ring-value small { font-size: 24px; }
</style>
</head>
<body>
<div class="stage">
  <div class="diversity-panel"></div>

  <svg class="graphics" viewBox="0 0 1500 1227" aria-hidden="true">
    <defs>
      <symbol id="woman" viewBox="0 0 54 126">
        <circle cx="27" cy="12" r="11"/>
        <path d="M17 26 H37 L44 38 L52 60 L47 62 L40 46 L46 84 H8 L14 46 L7 62 L2 60 L10 38 Z"/>
        <rect x="15" y="84" width="9" height="42" rx="4"/>
        <rect x="30" y="84" width="9" height="42" rx="4"/>
      </symbol>
      <symbol id="man" viewBox="0 0 60 128">
        <circle cx="30" cy="12" r="12"/>
        <path d="M14 27 H46 Q54 29 56 38 L59 72 H53 L49 46 V80 H11 V46 L7 72 H1 L4 38 Q6 29 14 27 Z"/>
        <rect x="14" y="78" width="13" height="50" rx="5"/>
        <rect x="33" y="78" width="13" height="50" rx="5"/>
        <path d="M30 28 L33 34 L30 52 L27 34 Z" fill="#ffffff"/>
      </symbol>
      <linearGradient id="bandFade" x1="0" x2="1">
        <stop offset="0" stop-color="var(--band)"/>
        <stop offset="1" stop-color="var(--band)" stop-opacity="0"/>
      </linearGradient>
    </defs>

    <!-- diversity donut -->
    <g fill="none" stroke-width="108" transform="rotate(-90 517 770)">
      <circle cx="517" cy="770" r="186" stroke="var(--navy)" stroke-dasharray="695.2 2000" stroke-dashoffset="-3"/>
      <circle cx="517" cy="770" r="186" stroke="var(--blue)" stroke-dasharray="274.5 2000" stroke-dashoffset="-704.2"/>
      <circle cx="517" cy="770" r="186" stroke="var(--sky)" stroke-dasharray="87.5 2000" stroke-dashoffset="-984.7"/>
      <circle cx="517" cy="770" r="186" stroke="var(--mist)" stroke-dasharray="87.5 2000" stroke-dashoffset="-1078.2"/>
    </g>
    <path d="M269 900 A280 280 0 0 0 765 900" fill="none" stroke="#6a9fd6" stroke-width="2" stroke-dasharray="8 7"/>

    <!-- leader lines -->
    <g fill="none" stroke="#2b2b2b" stroke-width="1.3">
      <polyline points="247,495 379,495 379,620"/>
      <polyline points="723,499 471,499 471,602"/>
      <polyline points="337,794 155,794 155,923"/>
      <polyline points="690,756 820,756 820,932"/>
    </g>
    <g fill="var(--accent)" stroke="#ffffff" stroke-width="1.5">
      <circle cx="379" cy="620" r="5"/>
      <circle cx="471" cy="602" r="5"/>
      <circle cx="337" cy="794" r="5"/>
      <circle cx="690" cy="756" r="5"/>
    </g>

    <!-- right column section markers -->
    <g stroke="#9aa4ae" stroke-width="1.2">
      <line x1="1025" y1="150" x2="1025" y2="220"/>
      <line x1="1025" y1="425" x2="1025" y2="495"/>
      <line x1="1025" y1="680" x2="1025" y2="752"/>
      <line x1="1025" y1="895" x2="1025" y2="965"/>
    </g>
    <g fill="url(#bandFade)">
      <rect x="1027" y="170" width="345" height="34"/>
      <rect x="1027" y="446" width="385" height="34"/>
      <rect x="1027" y="702" width="385" height="34"/>
      <rect x="1027" y="912" width="440" height="34"/>
    </g>
    <g fill="var(--accent)">
      <circle cx="1025" cy="186" r="4.5"/>
      <circle cx="1025" cy="463" r="4.5"/>
      <circle cx="1025" cy="718" r="4.5"/>
      <circle cx="1025" cy="929" r="4.5"/>
    </g>

    <!-- age chart -->
    <g stroke="var(--rule)" stroke-width="1">
      <line x1="1097" y1="229" x2="1409" y2="229"/>
      <line x1="1097" y1="256" x2="1409" y2="256"/>
      <line x1="1097" y1="283" x2="1409" y2="283"/>
      <line x1="1097" y1="310" x2="1409" y2="310"/>
      <line x1="1097" y1="338" x2="1409" y2="338"/>
      <line x1="1097" y1="365" x2="1409" y2="365"/>
      <line x1="1097" y1="392" x2="1409" y2="392"/>
    </g>
    <rect x="1119" y="305" width="66" height="87" fill="var(--navy)"/>
    <rect x="1219" y="240" width="70" height="152" fill="var(--blue)"/>
    <rect x="1321" y="360" width="74" height="32" fill="var(--sky)"/>

    <!-- gender: 40% male / 60% female -->
    <use href="#man" x="1182" y="500" width="60" height="128" fill="var(--navy)"/>
    <use href="#woman" x="1269" y="502" width="54" height="126" fill="var(--blue)"/>
    <rect x="1045" y="640" width="150" height="18" rx="9" fill="var(--navy)"/>
    <rect x="1180" y="640" width="217" height="18" rx="9" fill="var(--blue)"/>
    <circle cx="1186" cy="649" r="17" fill="var(--accent)" stroke="#ffffff" stroke-width="3"/>

    <!-- executive officers -->
    <use href="#woman" x="1052" y="758" width="54" height="126" fill="var(--blue)"/>
    <use href="#woman" x="1114" y="758" width="54" height="126" fill="var(--blue)"/>
    <use href="#man" x="1185" y="756" width="60" height="128" fill="var(--navy)"/>

    <!-- board composition -->
    <g fill="none" stroke="var(--navy)" stroke-width="15">
      <path d="M1058 1026 A62 62 0 0 1 1180 1026"/>
      <path d="M1180 1038 A62 62 0 0 1 1058 1038"/>
    </g>
    <use href="#woman" x="1225" y="968" width="54" height="126" fill="var(--blue)"/>
    <use href="#woman" x="1298" y="968" width="54" height="126" fill="var(--blue)"/>
    <use href="#woman" x="1370" y="968" width="54" height="126" fill="var(--navy)"/>
  </svg>

  <div class="team-art" role="img" aria-label="Illustration of a team of five business people standing together"></div>
  <div class="t title-our">OUR</div>
  <div class="t title-main">WORKFORCE</div>

  <div class="avatar me" role="img" aria-label="Portrait illustration of a Middle-Eastern employee"></div>
  <div class="avatar hi" role="img" aria-label="Portrait illustration of a Hispanic employee"></div>
  <div class="avatar as" role="img" aria-label="Portrait illustration of an Asian employee"></div>
  <div class="avatar wh" role="img" aria-label="Portrait illustration of a White employee"></div>

  <div class="t c pct-big" style="left:165px;top:603px;">8%</div>
  <div class="t c group-label" style="left:157px;top:641px;">Middle-Eastern</div>
  <div class="t c pct-big" style="left:807px;top:603px;">8%</div>
  <div class="t c group-label" style="left:805px;top:641px;">Hispanic</div>
  <div class="t c pct-big" style="left:160px;top:1108px;">24%</div>
  <div class="t c group-label" style="left:154px;top:1151px;">Asian</div>
  <div class="t c pct-big" style="left:826px;top:1115px;">60%</div>
  <div class="t c group-label" style="left:826px;top:1156px;">White</div>

  <div class="t c total-label">TOTAL<br>EMPLOYEES</div>
  <div class="t c total-value">25</div>
  <div class="t c diversity-label">DIVERSITY</div>

  <div class="t l section-title" style="left:1053px;top:188px;">AGE</div>
  <div class="t axis" style="right:408px;top:220px;">60%</div>
  <div class="t axis" style="right:408px;top:273px;">40%</div>
  <div class="t axis" style="right:408px;top:326px;">20%</div>
  <div class="t axis" style="right:408px;top:378px;">0</div>
  <div class="t c bar-val" style="left:1152px;top:351px;">32%</div>
  <div class="t c bar-val" style="left:1254px;top:351px;">56%</div>
  <div class="t c bar-val" style="left:1358px;top:378px;">12%</div>
  <div class="t c bar-cat" style="left:1152px;top:411px;">25 - 44</div>
  <div class="t c bar-cat" style="left:1251px;top:411px;">45 - 64</div>
  <div class="t c bar-cat" style="left:1357px;top:411px;">65+</div>

  <div class="t l section-title" style="left:1053px;top:464px;">GENDER</div>
  <div class="t c gender-pct male">40<small>%</small></div>
  <div class="t c gender-tag" style="left:1106px;top:618px;">MALE</div>
  <div class="t c gender-pct female">60<small>%</small></div>
  <div class="t c gender-tag" style="left:1363px;top:618px;">FEMALE</div>

  <div class="t l section-title" style="left:1053px;top:720px;">EXECUTIVE OFFICERS</div>
  <div class="t note" style="left:1264px;top:827px;">2 of 3 are<br>women</div>

  <div class="t l section-title" style="left:1053px;top:930px;">BOARD COMPOSITION</div>
  <div class="t c ring-value">50<small>%</small></div>
  <div class="t c note" style="left:1119px;top:1141px;">50% women<br>(3 directors)</div>
  <div class="t note" style="left:1229px;top:1105px;">One woman from<br>an unrepresented<br>community</div>
</div>
</body>
</html>
```